Tidy Trellis web design

I am after a web page design I can upload onto Site Build It! - which assists in building an ebusiness. I wish the site to have a vintage feel with a modern approach. I am fond of scroll or floral type motifs. As the web site will focus on home storage solutions, I would also like a practical feel too. I have a logo designed and ready to upload.

Target Market(s)

My target market is mature homeowners, particularly women who want stylish solutions to home storage.

Industry/Entity Type

Building

Requirements
Must have
• Logo to be prominent with co-ordinating background design. Navbar buttons to the left with similar background panel. far right column left available for associated links and advertisements.

```html
<!DOCTYPE html>
<html lang="en">
<head>
<meta charset="utf-8">
<title>Tidy Trellis – Home Storage Solutions</title>
<link rel="stylesheet" href="https://fonts.googleapis.com/css2?family=Questrial&family=Arimo:wght@400;700&display=swap">
<style>
  :root {
    --bg-dark: #9a9a9a;
    --bg-light: #d9d9d9;
    --card: #f3f3f3;
    --card-edge: #ffffff;
    --ink: #1c1c1c;
    --ink-soft: #3a3a3a;
    --ink-muted: #555555;
    --slate: #3b4a5c;
    --rule: #d6d6d6;
    --panel: #ececec;
    --panel-edge: #d3d3d3;
    --button-top: #5d5d5d;
    --button-bottom: #2b2b2b;
    --olive: #8a9a52;
    --olive-dark: #6f7f3a;
    --accent-orange: #e88a12;
    --footer-sep: #c77b2a;
    --hero-green-a: #5c7a34;
    --hero-green-b: #6d8a40;
    --hero-wall: #e9e6df;
    --white: #ffffff;
    --social-a: #3b5a9a;
    --social-b: #37a9dc;
  }
  * { box-sizing: border-box; margin: 0; padding: 0; }
  html, body { width: 1200px; height: 1022px; overflow: hidden; }
  body {
    position: relative;
    font-family: "Questrial", "Century Gothic", sans-serif;
    color: var(--ink);
    background: radial-gradient(ellipse at 40% 40%, var(--bg-light) 0%, #c3c3c3 55%, var(--bg-dark) 100%);
  }
  .page-texture { position: absolute; inset: 0; }
  .site {
    position: absolute; left: 158px; top: 26px; width: 881px; height: 948px;
    background: var(--card);
    border-radius: 10px;
    box-shadow: 0 0 14px rgba(0,0,0,.25);
    overflow: hidden;
  }
  .brand {
    position: absolute; left: 24px; top: 30px;
    display: flex; align-items: center; gap: 8px;
  }
  .brand-dot { width: 22px; height: 22px; border-radius: 50%; background: var(--slate); }
  .brand-name { font-size: 31px; color: var(--slate); letter-spacing: -0.5px; }

  .main-nav {
    position: absolute; left: 29px; top: 92px;
    display: flex; font-size: 13.5px; color: var(--ink); white-space: nowrap;
  }
  .main-nav span { padding: 0 11px; }
  .main-nav span:first-child { padding-left: 0; }
  .main-nav .sep { padding: 0; color: var(--ink); }

  .search {
    position: absolute; left: 641px; top: 90px; display: flex;
    height: 23px;
  }
  .search-field {
    width: 155px; border: 1px solid #c8c8c8; border-right: none; background: var(--white);
    font-family: "Arimo", Arial, sans-serif; font-size: 10.5px; color: #444;
    padding: 5px 10px; border-radius: 2px 0 0 2px;
  }
  .search-button {
    width: 62px; background: linear-gradient(var(--button-top), var(--button-bottom));
    color: var(--white); font-family: "Arimo", Arial, sans-serif; font-size: 11px;
    padding: 5px 0 0 7px; border-radius: 0 2px 2px 0; position: relative;
  }
  .search-button::after {
    content: ""; position: absolute; right: 8px; top: 8px;
    border-left: 5px solid var(--white); border-top: 3.5px solid transparent; border-bottom: 3.5px solid transparent;
  }

  .hero {
    position: absolute; left: 24px; top: 131px; width: 836px; height: 269px;
    border: 3px solid var(--card-edge); border-radius: 4px;
    box-shadow: 0 1px 4px rgba(0,0,0,.25);
    overflow: hidden;
  }
  .hero-photo {
    position: absolute; inset: 0;
    background:
      linear-gradient(180deg, transparent 78%, #d9d6cf 78%, #cfcac1 100%),
      linear-gradient(90deg, var(--hero-green-a) 0%, var(--hero-green-b) 60%, #6a8740 75%, var(--hero-wall) 76%, var(--hero-wall) 100%);
  }
  .hero-piece {
    position: absolute; left: 460px; top: 100px; width: 250px; height: 114px;
    background: #3f4756; border-radius: 2px;
  }
  .hero-title {
    position: absolute; left: 50px; top: 20px; color: var(--white);
    font-size: 53px; line-height: 48px; font-weight: 400;
  }
  .hero-title .line-1 { display: block; padding-left: 34px; }
  .hero-title .line-2 { display: block; }
  .hero-title .line-3 { display: block; padding-left: 30px; }
  .hero-copy {
    position: absolute; left: 48px; top: 180px; color: #eef2e6;
    font-size: 16.5px; line-height: 19px;
  }
  .hero-copy .read-more { color: var(--accent-orange); font-family: "Arimo", Arial, sans-serif; font-weight: 700; font-size: 13.5px; }

  .category-nav { position: absolute; left: 24px; top: 425px; width: 196px; }
  .category-nav li {
    list-style: none; height: 28.4px; line-height: 28.4px;
    padding-left: 21px; font-size: 13px; color: var(--ink);
    border-bottom: 1px solid var(--rule);
  }
  .category-nav li.is-active {
    background: linear-gradient(#e4e4e4, #d8d8d8); font-weight: 700;
    font-family: "Arimo", Arial, sans-serif; font-size: 11px; position: relative;
  }
  .category-nav li.is-active::before {
    content: ""; position: absolute; left: 8px; top: 10px;
    border-left: 4px solid var(--ink); border-top: 4px solid transparent; border-bottom: 4px solid transparent;
  }

  .side-box {
    position: absolute; left: 22px; width: 197px;
    background: var(--panel); border: 1px solid var(--panel-edge); border-radius: 2px;
  }
  .cart { top: 692px; height: 88px; }
  .subscribe { top: 795px; height: 94px; }
  .side-box h3 { font-weight: 400; font-size: 15px; color: var(--ink-soft); position: absolute; left: 14px; top: 10px; }
  .cart h3 { font-size: 14.5px; letter-spacing: .3px; }
  .side-box p {
    position: absolute; left: 14px; font-family: "Arimo", Arial, sans-serif;
    font-size: 10.5px; line-height: 17px; color: var(--ink);
  }
  .cart p { top: 38px; width: 150px; }
  .subscribe p { top: 26px; font-size: 10px; }
  .cart-icon { position: absolute; right: 10px; top: 8px; }
  .email-field {
    position: absolute; left: 15px; top: 52px; width: 166px; height: 20px;
    background: var(--white); border: 1px solid #9c9c9c;
    font-family: "Arimo", Arial, sans-serif; font-size: 10px; padding: 4px 6px;
  }

  .featured { position: absolute; left: 252px; top: 430px; width: 410px; height: 460px; }
  .featured h2 {
    font-family: "Arimo", Arial, sans-serif; font-weight: 700; font-size: 12px;
    color: var(--ink-soft); position: absolute; left: 0; top: 1px;
  }
  .product { position: absolute; width: 140px; text-align: center; font-family: "Arimo", Arial, sans-serif; }
  .product-photo { width: 110px; margin: 0 auto; border-radius: 3px; }
  .product-name { font-size: 11.5px; color: var(--ink); margin-top: 14px; }
  .product-price { font-size: 11.5px; font-weight: 700; margin-top: 4px; }
  .add-to-cart {
    display: block; width: 98px; height: 20px; margin: 8px auto 0;
    background: linear-gradient(var(--button-top), var(--button-bottom));
    color: var(--white); font-size: 10.5px; line-height: 20px; border-radius: 2px;
  }
  .listing-count {
    position: absolute; left: 1px; top: 438px; font-family: "Arimo", Arial, sans-serif;
    font-size: 10.5px; color: var(--ink-muted); font-weight: 700;
  }
  .pager {
    position: absolute; left: 306px; top: 438px; font-family: "Arimo", Arial, sans-serif;
    font-size: 10.5px; color: var(--ink-muted); font-weight: 700;
  }

  .links-box {
    position: absolute; left: 677px; top: 416px; width: 184px; height: 146px;
    background: var(--panel); border: 1px solid var(--panel-edge);
  }
  .links-box h3 { font-weight: 400; font-size: 14px; color: var(--ink-soft); position: absolute; left: 14px; top: 11px; }
  .links-box ul { position: absolute; left: 12px; top: 40px; list-style: none; }
  .links-box li { font-size: 12.5px; height: 24.6px; display: flex; align-items: center; gap: 10px; }
  .bullet {
    width: 13px; height: 13px; border-radius: 50%;
    background: radial-gradient(circle at 40% 35%, #c5cf8f, var(--olive-dark));
  }

  .promo {
    position: absolute; left: 677px; top: 576px; width: 184px; height: 310px;
    background: var(--white); border: 1px solid var(--panel-edge); overflow: hidden;
  }
  .promo-headline {
    position: absolute; left: 6px; top: 6px; font-family: "Arimo", Arial, sans-serif;
    font-weight: 700; font-size: 37px; color: var(--olive); letter-spacing: -1px;
  }
  .promo-sub {
    position: absolute; right: 12px; top: 50px; font-family: "Arimo", Arial, sans-serif;
    font-size: 11.5px; color: var(--olive-dark);
  }
  .promo-photo {
    position: absolute; left: 0; top: 72px; width: 100%; height: 238px;
    background: linear-gradient(180deg, #f4f1ea 0%, #f0ebe2 65%, #e7c9b4 100%);
  }
  .promo-piece {
    position: absolute; left: 20px; top: 62px; width: 140px; height: 140px;
    background: #ec6a1e; border-radius: 2px;
  }

  .site-footer {
    position: absolute; left: 0; top: 905px; width: 100%; height: 43px;
    background: linear-gradient(#e6e6e6, #dadada);
    font-family: "Arimo", Arial, sans-serif; font-size: 10.5px;
  }
  .copyright { position: absolute; left: 22px; top: 17px; font-weight: 700; color: var(--ink-soft); }
  .footer-links { position: absolute; right: 67px; top: 18px; color: var(--ink); }
  .footer-links .sep { color: var(--footer-sep); margin: 0 5px; }
  .social { position: absolute; top: 13px; width: 18px; height: 18px; border-radius: 3px; }
  .social-a { right: 38px; background: var(--social-a); }
  .social-b { right: 10px; background: var(--social-b); }
</style>
</head>
<body>
  <div class="page-texture" role="img" aria-label="Soft grey textured backdrop with faint floral scroll flourishes"></div>

  <div class="site">
    <header>
      <div class="brand">
        <span class="brand-dot"></span>
        <span class="brand-name">tidytrellis</span>
      </div>

      <nav class="main-nav">
        <span>HOME PAGE</span><span class="sep">|</span>
        <span>NEW PRODUCTS</span><span class="sep">|</span>
        <span>SPECIALS</span><span class="sep">|</span>
        <span>ALL PRODUCTS</span><span class="sep">|</span>
        <span>CONTACT US</span><span class="sep">|</span>
        <span>FAQS</span>
      </nav>

      <div class="search">
        <div class="search-field">Search Our Products</div>
        <div class="search-button">Search</div>
      </div>
    </header>

    <section class="hero">
      <div class="hero-photo" role="img" aria-label="Dark grey storage sideboard with books against a green wall beside a white chair, with a scroll flourish">
        <div class="hero-piece"></div>
      </div>
      <h1 class="hero-title">
        <span class="line-1">Get</span>
        <span class="line-2">Organized</span>
        <span class="line-3">for Spring!</span>
      </h1>
      <p class="hero-copy">tidytrellis has everything you need to<br>start your spring off on the right foot <span class="read-more">Read More</span></p>
    </section>

    <ul class="category-nav">
      <li class="is-active">FEATURED PRODUCTS</li>
      <li>SPECIALS</li>
      <li>BEDROOM</li>
      <li>FAMILY ROOM</li>
      <li>GARAGE</li>
      <li>HOME OFFICE</li>
      <li>KITCHEN</li>
      <li>LAUNDRY</li>
      <li>UTILITY</li>
    </ul>

    <aside class="side-box cart">
      <h3>MY CART</h3>
      <svg class="cart-icon" width="28" height="22" viewBox="0 0 28 22" fill="none" stroke="#8a8a8a" stroke-width="1.6">
        <path d="M1 2h5l3 12h14l3-9H8"/>
        <circle cx="11" cy="18.5" r="1.8"/><circle cx="21" cy="18.5" r="1.8"/>
      </svg>
      <p>You currently have no items in your shopping cart</p>
    </aside>

    <aside class="side-box subscribe">
      <h3>Subscribe</h3>
      <p>Be Notied of upcoing News and Deals</p>
      <div class="email-field">Enter Your Email.</div>
    </aside>

    <main class="featured">
      <h2>FEATURED PRODUCTS</h2>

      <div class="product" style="left:-14px;top:27px">
        <div class="product-photo" role="img" aria-label="Chrome mesh stacking drawer unit" style="height:112px;background:linear-gradient(#e2e4e6,#b9bdc1)"></div>
        <div class="product-name">Mesh Stacking Selves</div>
        <div class="product-price">$119.00</div>
        <span class="add-to-cart">Add to Cart</span>
      </div>
      <div class="product" style="left:131px;top:27px">
        <div class="product-photo" role="img" aria-label="Beige cotton garment bags on a rail" style="height:112px;background:linear-gradient(#f1e8d8,#d8c6a6)"></div>
        <div class="product-name">Cotton Garment Bags</div>
        <div class="product-price">$29.99</div>
        <span class="add-to-cart">Add to Cart</span>
      </div>
      <div class="product" style="left:272px;top:27px">
        <div class="product-photo" role="img" aria-label="Rolling garment rack with hanging clothes" style="height:112px;background:linear-gradient(#ece8e2,#c8bfb2)"></div>
        <div class="product-name">Garment Rack</div>
        <div class="product-price">$69.00</div>
        <span class="add-to-cart">Add to Cart</span>
      </div>

      <div class="product" style="left:-14px;top:242px">
        <div class="product-photo" role="img" aria-label="Grey zippered underbed storage bag" style="height:94px;background:linear-gradient(#d9d9d9,#9d9d9d)"></div>
        <div class="product-name">Underbed Bag</div>
        <div class="product-price">$14.99</div>
        <span class="add-to-cart">Add to Cart</span>
      </div>
      <div class="product" style="left:131px;top:242px">
        <div class="product-photo" role="img" aria-label="Black clear-pocket handbag organizer" style="height:94px;background:linear-gradient(#5a5a5a,#1f1f1f)"></div>
        <div class="product-name">Handbag Organizer</div>
        <div class="product-price">$11.99</div>
        <span class="add-to-cart">Add to Cart</span>
      </div>
      <div class="product" style="left:272px;top:242px">
        <div class="product-photo" role="img" aria-label="Woven and dark fabric storage bins" style="height:94px;background:linear-gradient(#e6d6b6,#55504a)"></div>
        <div class="product-name">Storage Bin</div>
        <div class="product-price">$12.99</div>
        <span class="add-to-cart">Add to Cart</span>
      </div>

      <div class="listing-count">Displaying 1 to 10 (of 20 products)</div>
      <div class="pager">1 2 [ Next&gt;&gt;]</div>
    </main>

    <aside class="links-box">
      <h3>ASSOCIATED LINKS</h3>
      <ul>
        <li><span class="bullet"></span>tidytrellis one</li>
        <li><span class="bullet"></span>tidytrellis two</li>
        <li><span class="bullet"></span>tidytrellis three</li>
        <li><span class="bullet"></span>tidytrellis four</li>
      </ul>
    </aside>

    <aside class="promo">
      <div class="promo-headline">40% OFF</div>
      <div class="promo-sub">SELECTED ITEMS</div>
      <div class="promo-photo" role="img" aria-label="Orange open shelving unit with books and a vase of flowers">
        <div class="promo-piece"></div>
      </div>
    </aside>

    <footer class="site-footer">
      <div class="copyright">© 2011 Tidy Trellis. All Rights Reserved.</div>
      <div class="footer-links">
        Bedroom<span class="sep">|</span>Family Room<span class="sep">|</span>Garage<span class="sep">|</span>Home Office<span class="sep">|</span>Kitchen<span class="sep">|</span>Laundry<span class="sep">|</span>Utility<span class="sep">|</span>Follow
      </div>
      <span class="social social-a"></span>
      <span class="social social-b"></span>
    </footer>
  </div>
</body>
</html>
```